KL MOTORS BANNER/SIGN DESIGN

Design a banner sign for outdoor use for KL MOTORS - a premium pre owned vehicle sales center. The size must be 36 feet in width
and 3 feet in height.

Information required: logo (attached)
-PREMIUM PRE-OWEND VEHICLE SALES
- 517.264.3081

perhaps in smaller font: BUY-SELL-TRADE

prefer white background but could possibly do red matching the logo

```html
<!DOCTYPE html>
<html lang="en">
<head>
<meta charset="utf-8">
<title>KL Motors Banner</title>
<link href="https://fonts.googleapis.com/css2?family=Michroma&family=Open+Sans:wght@400&display=swap" rel="stylesheet">
<style>
  :root {
    --bg: #ffffff;
    --ink: #111111;
    --red: #d0141b;
    --mist: #cfe4f4;
    --mist-soft: rgba(207, 228, 244, 0);
    --car: #e4e6e8;
    --car-dark: #8a8f94;
  }
  html, body {
    margin: 0;
    padding: 0;
    width: 1200px;
    height: 100px;
    overflow: hidden;
    background: var(--bg);
  }
  .banner {
    position: relative;
    width: 1200px;
    height: 100px;
    background: var(--bg);
    overflow: hidden;
  }
  .mist {
    position: absolute;
    top: 0;
    height: 100px;
    width: 280px;
  }
  .mist--left {
    left: 0;
    background: radial-gradient(ellipse 260px 70px at 60px 50px, var(--mist), var(--mist-soft) 75%);
  }
  .mist--right {
    right: 0;
    background: radial-gradient(ellipse 260px 70px at 240px 45px, var(--mist), var(--mist-soft) 75%);
  }
  .brand {
    position: absolute;
    left: 12px;
    top: 30px;
    display: flex;
    align-items: center;
    gap: 10px;
  }
  .brand__mark {
    width: 40px;
    height: 40px;
    border-radius: 50%;
    background: var(--red);
  }
  .brand__name {
    font-family: "Michroma", sans-serif;
    font-size: 22px;
    color: var(--ink);
    letter-spacing: 1px;
  }
  .headline {
    position: absolute;
    left: 0;
    right: 0;
    top: 14px;
    text-align: center;
    font-family: "Michroma", sans-serif;
    font-size: 22px;
    letter-spacing: 1.5px;
    color: var(--ink);
    margin: 0;
    font-weight: 400;
  }
  .services {
    position: absolute;
    left: 0;
    right: 0;
    top: 50px;
    display: flex;
    justify-content: center;
    align-items: center;
    gap: 14px;
  }
  .services__text {
    font-family: "Open Sans", sans-serif;
    font-size: 35px;
    line-height: 40px;
    color: var(--red);
  }
  .car-photo {
    width: 36px;
    height: 20px;
    border-radius: 8px 10px 4px 4px;
    background: linear-gradient(180deg, var(--car), var(--car-dark));
  }
  .contact {
    position: absolute;
    left: 930px;
    top: 36px;
    display: flex;
    align-items: center;
    gap: 10px;
  }
  .contact__icon {
    width: 20px;
    height: 20px;
  }
  .contact__phone {
    font-family: "Michroma", sans-serif;
    font-size: 22px;
    letter-spacing: 2px;
    color: var(--ink);
  }
</style>
</head>
<body>
  <div class="banner">
    <div class="mist mist--left" role="img" aria-label="Soft light blue smoke swirls"></div>
    <div class="mist mist--right" role="img" aria-label="Soft light blue smoke swirls"></div>

    <div class="brand">
      <span class="brand__mark"></span>
      <span class="brand__name">KL MOTORS</span>
    </div>

    <h1 class="headline">PREMIUM PRE-OWNED VEHICLE SALES</h1>

    <div class="services">
      <div class="car-photo" role="img" aria-label="White SUV photo"></div>
      <span class="services__text">BUY-SELL-TRADE</span>
      <div class="car-photo" role="img" aria-label="White SUV photo"></div>
    </div>

    <div class="contact">
      <svg class="contact__icon" viewBox="0 0 24 24" aria-hidden="true">
        <path fill="#d0141b" d="M6.6 10.8c1.4 2.8 3.8 5.1 6.6 6.6l2.2-2.2c.3-.3.7-.4 1-.2 1.1.4 2.3.6 3.6.6.6 0 1 .4 1 1V20c0 .6-.4 1-1 1C10.6 21 3 13.4 3 4c0-.6.4-1 1-1h3.5c.6 0 1 .4 1 1 0 1.3.2 2.5.6 3.6.1.3 0 .7-.2 1l-2.3 2.2z"/>
      </svg>
      <span class="contact__phone">517.264.3081</span>
    </div>
  </div>
</body>
</html>
```